Bold Cover needed for a book on Workplace Bullying

I need a book cover design for a book titled, “Iron Silence?” The book recounts my story of bullying in the workplace. It also includes chapters on how readers can minimize/stop workplace bullying, write an effective complaint, and ensure their own mental wellbeing.
I am looking for a bold design using red and black, and possibly distressed lettering. The covers of other books dealing with this subject do not reflect my vision. They are often too childish or look too academic. This book needs to stress the serious nature of a toxic workplace, while appealing to readers experiencing a similar situation. I’d like the cover to reflect the mental anguish associated with workplace bullying (hence the distressed lettering).
I have included a cover that appeals to me (although the coloring is wrong). That said, I am also very happy (and excited) to see your creative input!
On the cover, it should have the following:
Title: Iron Silence?
Subtitle: How the Harbour Works Department Condones Bullying & Ruins Lives
Author: Owen Frick
Other relevant details:
Book size: 5.5” x 8.5”
Back cover will have a blurb, author picture/short bio, and barcode
The blurb on the back cover reads:
Undermining, intimidation and threats
Despite the Department of Harbour Works allegedly holding a zero tolerance for bullying, these behaviours were an everyday occurrence in at least one workplace. Even after a decade of complaints, numerous witnesses and physical proof, the department failed to act. Instead, they looked the other way, allowing one powerful and well-connected individual to end careers and ruin lives.
After being targeted, one teacher resolved to put an end to the abuse experienced by more than fifty employees. His startling story reveals the relentless bullying, mental health ramifications, and insidious tactics used to cover up the corrosive behaviour.
Those who have experienced a toxic workplace will also find much needed support and guidance, intended to minimise suffering and detail a clear way forward. Chapters include dealing with bullying in the workplace, how to lodge a successful complaint, and how to stay sane during any potential legal action.

```html
<!DOCTYPE html>
<html lang="en">
<head>
<meta charset="utf-8">
<title>Iron Silence? — Book Cover</title>
<link href="https://fonts.googleapis.com/css2?family=Montserrat:wght@600&family=Teko:wght@500;600&display=swap" rel="stylesheet">
<style>
  :root {
    --backdrop: #022130;
    --cover-navy: #021f2e;
    --alarm-red: #e8444f;
    --chalk-white: #ececec;
  }
  html, body {
    margin: 0;
    width: 1200px;
    height: 926px;
    overflow: hidden;
    background: var(--backdrop);
  }
  .book-cover {
    position: absolute;
    left: 337px;
    top: 62px;
    width: 526px;
    height: 803px;
    background: var(--cover-navy);
  }
  .subtitle {
    position: absolute;
    top: 28px;
    left: 0;
    width: 100%;
    margin: 0;
    text-align: center;
    font-family: "Montserrat", sans-serif;
    font-weight: 600;
    font-size: 21px;
    line-height: 28px;
    letter-spacing: 0.2px;
    color: var(--chalk-white);
    text-transform: uppercase;
  }
  .cover-art {
    position: absolute;
    inset: 0;
  }
  .question-mark { fill: var(--alarm-red); }
  .title-word {
    font-family: "Teko", sans-serif;
    font-weight: 600;
    fill: var(--chalk-white);
  }
  .author-name {
    font-family: "Teko", sans-serif;
    font-weight: 500;
    fill: var(--chalk-white);
  }
</style>
</head>
<body>
  <main class="book-cover">
    <h2 class="subtitle">How the Harbour Works Department<br>Condones Bullying &amp; Ruins Lives</h2>
    <svg class="cover-art" viewBox="0 0 526 803" width="526" height="803" aria-labelledby="cover-title">
      <title id="cover-title">Iron Silence? by Owen Frick</title>
      <path class="question-mark" d="M100,198 C150,140 215,111 280,111 C380,111 447,170 447,258 C447,330 400,370 360,405 C330,432 318,455 318,490 L318,560 L214,560 L214,490 C214,430 240,395 285,355 C320,325 346,300 346,262 C346,222 318,194 280,194 C240,194 200,220 162,255 Z"/>
      <rect class="question-mark" x="214" y="655" width="104" height="31"/>
      <text class="title-word" x="150" y="584" textLength="248" lengthAdjust="spacingAndGlyphs" font-size="176">IRON</text>
      <text class="title-word" x="150" y="648" textLength="248" lengthAdjust="spacingAndGlyphs" font-size="80">SILENCE</text>
      <text class="author-name" x="54" y="770" textLength="440" lengthAdjust="spacing" font-size="48">OWEN FRICK</text>
    </svg>
  </main>
</body>
</html>
```